Serenity Prayer Art/Poster Design for Canvas Printing

I have been tasked with creating a piece of art containing the complete serenity prayer for a rehab in New York. The final design will essentially be split into 3 sections and printed on 3 canvases which will hang together (please see below for detailed final product requirements).

We are looking for something that has a classic feel to it, but itsn't overly flourish-y or cheezy as many "church-y" things can feel. Fonts similar to that used in the uploaded file are probably the safest but we don't want to inhibit what you would come up with creatively on your own. I am looking for some sort of background behind the words. This can be a picture, ambiance (sort of like in the attached file). It should be beautiful, refreshing and stunning to look at.

Please feel free to use any Harbor Fellowship symbols or colors (feel free to google, "The Harbor Fellowship Flag" "The Harbor Fellowship Crest" "The Harbor Fellowship Shield") in an abstract way in the background. I would not be looking for any literal or exact Fellowship symbols to appear, but using shadows, outlines, etc. is completely acceptable. I'm attaching some CD art which uses The Harbor Fellowship shield in the way I am describing. The words "The Harbor Fellowship" are removed and it is the outline of the shield used in a very modern, simplistic way. Red, Yellow and Blue would be the colors to use ideally as these are the colors of The Harbor Fellowship... you could even get creative and use a different color on each panel.

In the file you will find the complete Serenity prayer. The only words we want on the artwork is:

"God grant me the serenity to accept the things I cannot change; courage to change the things I can; and wisdom to know the difference. Living one day at a time; Enjoying one moment at a time; Accepting hardships as the pathway to peace; Taking, as He did, this sinful world as it is, not as I would have it; Trusting that He will make all things right if I surrender to His Will; That I may be reasonably happy in this life and supremely happy with Him forever in the next. Amen.

- Lambert Osgoodson
Commissioned by Majors Daniel & Fern Oakes"

Please do not italicize the font as it is in the reference.

We are printing the 3 sections on canvases sized 24"w x 48"h. Since there is a folded border that is 1.5" deep, the total size of the artwork should be 75"w x 51"h and we would be expecting 3 files each measuring 27"w x 51"h (to allow room for the border of each canvas while maintaining the integrity of the image as a whole). If there is any confusion as to what we are looking for in terms of dimensions or images, please let me know. It's much simpler than it seems.

I am attaching a VERY rough doodle of the layout to help with any questions.

We want something that is beautiful and inspiring and can't wait to see what you work on!

Target Market(s)

Will be used as hanging art in a rehab center.

Industry/Entity Type

Printing

Font styles to use
Other font styles liked:
• Can be a nice, modern Script font or somethings like Sans Serif.

Colors
0555a3
ec1f27
fbed22
85acd3
f59296
fbf289

Requirements
Must have
• The Serenity Prayer as noted in the notes.
Nice to have
• Modern, abstract use of a Harbor Fellowship symbol in the background somehow.

```html
<!DOCTYPE html>
<html lang="en">
<head>
<meta charset="utf-8">
<title>Serenity Prayer Triptych</title>
<link rel="stylesheet" href="https://fonts.googleapis.com/css2?family=Crimson+Text:wght@400&display=swap">
<style>
  :root {
    --blue: #0b4aa8;
    --blue-deep: #0a3f9c;
    --red: #e8332b;
    --red-soft: #ec5a3a;
    --orange: #f2a23c;
    --yellow: #f0cf4e;
    --yellow-pale: #e9e07a;
    --sage: #b7c46a;
    --teal: #5f9a9a;
    --panel-line: rgba(60, 40, 40, 0.55);
    --ink: #ffffff;
  }
  * { margin: 0; padding: 0; box-sizing: border-box; }
  html, body {
    width: 1200px;
    height: 820px;
    overflow: hidden;
    background: #ffffff;
  }
  .triptych {
    position: relative;
    width: 1200px;
    height: 820px;
    overflow: hidden;
    background:
      radial-gradient(ellipse 330px 260px at 230px 190px, var(--blue) 0%, rgba(11,74,168,0.85) 40%, rgba(11,74,168,0) 100%),
      radial-gradient(ellipse 420px 230px at 620px 70px, var(--blue-deep) 0%, rgba(10,63,156,0.9) 45%, rgba(10,63,156,0) 100%),
      radial-gradient(ellipse 300px 260px at 960px 130px, var(--blue) 0%, rgba(11,74,168,0.75) 45%, rgba(11,74,168,0) 100%),
      radial-gradient(ellipse 220px 200px at 1150px 250px, rgba(95,154,154,0.8) 0%, rgba(95,154,154,0) 100%),
      radial-gradient(ellipse 260px 320px at 30px 520px, var(--red-soft) 0%, rgba(236,90,58,0.6) 45%, rgba(236,90,58,0) 100%),
      radial-gradient(ellipse 360px 200px at 600px 830px, var(--red) 0%, rgba(232,51,43,0.7) 40%, rgba(232,51,43,0) 100%),
      radial-gradient(ellipse 320px 260px at 160px 700px, rgba(242,162,60,0.8) 0%, rgba(242,162,60,0) 100%),
      radial-gradient(ellipse 240px 260px at 40px 60px, rgba(183,196,106,0.9) 0%, rgba(183,196,106,0) 100%),
      radial-gradient(ellipse 380px 360px at 1060px 600px, var(--yellow-pale) 0%, rgba(233,224,122,0) 100%),
      linear-gradient(180deg, #d6c35a 0%, var(--yellow) 55%, #efbd48 80%, var(--orange) 100%);
  }
  .triptych__emblem {
    position: absolute;
    left: 290px;
    top: 180px;
    width: 220px;
    height: 240px;
    border-radius: 50%;
    background: radial-gradient(circle, rgba(255,255,255,0.06) 0%, rgba(255,255,255,0) 70%);
  }
  .triptych__divider {
    position: absolute;
    top: 0;
    width: 2px;
    height: 820px;
    background: var(--panel-line);
  }
  .triptych__divider--left { left: 400px; }
  .triptych__divider--right { left: 802px; }
  .triptych__center {
    position: absolute;
    left: 402px;
    top: 0;
    width: 400px;
    height: 820px;
    background: rgba(40, 20, 60, 0.05);
  }
  .prayer {
    position: absolute;
    left: 402px;
    top: 104px;
    width: 400px;
    text-align: center;
    font-family: "Crimson Text", Georgia, serif;
    font-size: 18px;
    line-height: 35.6px;
    letter-spacing: 0.2px;
    color: var(--ink);
    text-shadow: 0 0 2px rgba(0,0,0,0.15);
  }
  .prayer__line { display: block; }
  .attribution {
    position: absolute;
    left: 431px;
    top: 703px;
    font-family: "Crimson Text", Georgia, serif;
    font-size: 17px;
    line-height: 24px;
    color: var(--ink);
  }
</style>
</head>
<body>
  <main class="triptych">
    <div class="triptych__emblem" role="img" aria-label="Faint abstract shield outline in the background"></div>
    <div class="triptych__center"></div>
    <div class="triptych__divider triptych__divider--left"></div>
    <div class="triptych__divider triptych__divider--right"></div>

    <p class="prayer">
      <span class="prayer__line">God grant me the serenity</span>
      <span class="prayer__line">to accept the things I cannot change;</span>
      <span class="prayer__line">courage to change the things I can;</span>
      <span class="prayer__line">and wisdom to know the difference.</span>
      <span class="prayer__line">Living one day at a time;</span>
      <span class="prayer__line">Enjoying one moment at a time;</span>
      <span class="prayer__line">Accepting hardships as the pathway to peace;</span>
      <span class="prayer__line">Taking, as He did, this sinful world</span>
      <span class="prayer__line">as it is, not as I would have it;</span>
      <span class="prayer__line">Trusting that He will make all things right</span>
      <span class="prayer__line">if I surrender to His Will;</span>
      <span class="prayer__line">That I may be reasonably happy in this life</span>
      <span class="prayer__line">and supremely happy with Him</span>
      <span class="prayer__line">Forever in the next.</span>
      <span class="prayer__line">Amen.</span>
    </p>

    <p class="attribution">
      - Lambert Osgoodson<br>
      Commissioned by Majors Daniel &amp; Fern Oakes
    </p>
  </main>
</body>
</html>
```